Graphic Design of Business Process

We require an eye-catching, sophisticated design of 2 business processes (attached), that will be used digitally AND for print (to be put on walls in our office).

The basic layout is attached. We require a creative, professional designer to re-design these so that they look appealing but still able to grasp all the information.

We will require vector files and editable project files for final delivery. You may refer to our website (kitefieldmedia.com.au) for an indication of our brand.

If you have any questions, please ask.

Thank you.

```html
<!DOCTYPE html>
<html lang="en">
<head>
<meta charset="utf-8">
<title>Sales Content Funnel</title>
<link rel="stylesheet" href="https://fonts.googleapis.com/css2?family=Montserrat:wght@400;600;700;800&family=Source+Sans+3:wght@300;400;600&display=swap">
<style>
  :root {
    --ink: #0b0b0b;
    --gold: #c2a70d;
    --stage-awareness: #cfba3b;
    --stage-consideration: #c2a707;
    --stage-action: #937f04;
    --stage-text: #fbf5dc;
    --paper: #ffffff;
  }
  html, body {
    margin: 0;
    padding: 0;
    width: 1200px;
    height: 902px;
    overflow: hidden;
    background: var(--paper);
  }
  .funnel-chart { display: block; width: 1200px; height: 902px; }
  .title { font-family: "Montserrat", sans-serif; font-weight: 800; font-size: 70px; }
  .title-dark { fill: var(--ink); }
  .title-gold { fill: var(--gold); }
  .funnel-backdrop { fill: var(--ink); }
  .stage-awareness { fill: var(--stage-awareness); }
  .stage-consideration { fill: var(--stage-consideration); }
  .stage-action { fill: var(--stage-action); }
  .stage-name { font-family: "Montserrat", sans-serif; font-weight: 400; font-size: 35px; fill: var(--stage-text); letter-spacing: 0.5px; }
  .stage-goal { font-family: "Montserrat", sans-serif; font-weight: 400; font-size: 17px; fill: var(--stage-text); }
  .stage-point { font-family: "Montserrat", sans-serif; font-weight: 400; font-size: 14px; fill: var(--stage-text); }
  .stage-point .strong { font-weight: 700; }
  .divider { stroke: var(--stage-text); stroke-width: 1.5; }
  .bullet { fill: var(--stage-text); }
  .connector { stroke: var(--gold); stroke-width: 2; fill: none; }
  .arrow-head { fill: var(--gold); }
  .note-head { font-family: "Source Sans 3", sans-serif; font-weight: 600; font-size: 26px; }
  .note-head .dark { fill: var(--ink); }
  .note-head .gold { fill: var(--gold); }
  .note-body { font-family: "Source Sans 3", sans-serif; font-weight: 300; font-size: 21px; fill: var(--ink); }
  .loop-label { font-family: "Montserrat", sans-serif; font-weight: 600; font-size: 48px; }
  .loop-label .dark { fill: var(--ink); }
  .loop-label .gold { fill: var(--gold); }
</style>
</head>
<body>
<svg class="funnel-chart" viewBox="0 0 1500 1127.5" xmlns="http://www.w3.org/2000/svg" role="img" aria-label="Sales content funnel: awareness, consideration and action/decision, fed back by word of mouth and referral">

  <!-- Heading -->
  <text class="title" x="322" y="135"><tspan class="title-dark">SALES</tspan></text>
  <polygon class="title-dark" points="562,88 586,110 562,132"/>
  <polygon class="title-gold" points="605,88 630,110 605,132"/>
  <text class="title title-gold" x="646" y="135">CONTENT FUNNEL</text>

  <!-- Funnel -->
  <polygon class="funnel-backdrop" points="145,270 852,270 498,875"/>
  <polygon class="stage-awareness" points="72,306 920,306 828,470 165,470"/>
  <polygon class="stage-consideration" points="185,503 807,503 708,676 285,676"/>
  <polygon class="stage-action" points="303,708 688,708 496,1040"/>

  <!-- Awareness -->
  <text class="stage-name" x="496" y="352" text-anchor="middle">AWARENESS</text>
  <line class="divider" x1="359" y1="369" x2="359" y2="394"/>
  <text class="stage-goal" x="375" y="387">IDENTIFY PROBLEM/NEED</text>
  <polygon class="bullet" points="343,414 348,419 343,424"/>
  <text class="stage-point" x="355" y="425">ASPIRATIONAL</text>
  <polygon class="bullet" points="343,432 348,437 343,442"/>
  <text class="stage-point" x="355" y="443">MARKET THE <tspan class="strong">OUTCOME</tspan>, NOT PRODUCT</text>

  <!-- Consideration -->
  <text class="stage-name" x="496" y="554" text-anchor="middle">CONSIDERATION</text>
  <line class="divider" x1="368" y1="576" x2="368" y2="601"/>
  <text class="stage-goal" x="381" y="594">EVALUATE ALTERNATIVES</text>
  <polygon class="bullet" points="292,623 297,628 292,633"/>
  <text class="stage-point" x="307" y="634">WHY IS T<tspan class="strong">HIS SOLUTION</tspan> BETTER THAN OTHERS</text>
  <polygon class="bullet" points="292,641 297,646 292,651"/>
  <text class="stage-point" x="307" y="652"><tspan class="strong">HOW</tspan> IS THIS PROVIDER GOING TO SOLVE MY NEED</text>

  <!-- Action / Decision -->
  <text class="stage-name" x="496" y="760" text-anchor="middle">ACTION/</text>
  <text class="stage-name" x="496" y="799" text-anchor="middle">DECISION</text>
  <line class="divider" x1="399" y1="820" x2="399" y2="845"/>
  <text class="stage-goal" x="412" y="838">PRESENT AN OFFER</text>
  <polygon class="bullet" points="418,862 423,867 418,872"/>
  <text class="stage-point" x="431" y="873"><tspan class="strong">WHICH</tspan> PROVIDER?</text>

  <!-- Brackets and connectors -->
  <path class="connector" d="M868,395 H944 M960,326 H944 V467 H960"/>
  <path class="connector" d="M745,611 H820 M836,543 H820 V684 H836"/>
  <path class="connector" d="M605,848 H668 M684,817 H668 V887 H684"/>

  <!-- Stage notes -->
  <text class="note-head" x="973" y="372"><tspan class="dark">PROBLEM &amp; </tspan><tspan class="gold">SOLUTION</tspan></text>
  <text class="note-body" x="973" y="409">Subject showing symptoms</text>
  <text class="note-body" x="973" y="435">of Problem</text>

  <text class="note-head" x="854" y="589"><tspan class="dark">PROVIDERS &amp; </tspan><tspan class="gold">TYPE OF</tspan></text>
  <text class="note-head" x="854" y="623"><tspan class="gold">SOLUTION</tspan></text>
  <text class="note-body" x="854" y="660">Subject gives name to problem</text>

  <text class="note-head" x="689" y="860"><tspan class="dark">CONVERT &amp; </tspan><tspan class="gold">RETAIN</tspan></text>

  <!-- Word of mouth loop -->
  <path class="connector" d="M1370,363 V850 M1370,363 H1284 M1370,579 H1154 M1370,850 H954"/>
  <polygon class="arrow-head" points="1270,363 1286,353 1286,373"/>
  <polygon class="arrow-head" points="1140,579 1156,569 1156,589"/>
  <polygon class="arrow-head" points="940,850 956,840 956,860"/>

  <text class="loop-label" transform="translate(1389,398) rotate(90)"><tspan class="dark">WOM &amp; </tspan><tspan class="gold">REFERRAL</tspan></text>
</svg>
</body>
</html>
```